KTNW Unique Letterhead for Financial Services Business

I am looking for a letterhead design to match our branding colours. I do not want to see anything generic that could be created in word, I can do that myself, I am after something with a bit of designer flair. Once completed I will need files in a print ready format (including bleed area).

I have included our logo file and also our new business card design but get creative.

Industry/Entity Type

Financial Services

Font styles to use
Other font styles liked:
• raleway

Colors
00AB8E
00BBA5
67D7C9
C6EFE9
E9F9F6

Requirements
Must have
• Must be consisten with logo branding colours.
Should not have
• Anything generic that I could create myself in word

```html
<!DOCTYPE html>
<html lang="en">
<head>
<meta charset="utf-8">
<title>KTNW Financial Services – Letterhead</title>
<link href="https://fonts.googleapis.com/css2?family=Raleway:wght@400;500;600&family=Open+Sans:wght@400;700&display=swap" rel="stylesheet">
<style>
  :root {
    --teal-dark: #00566a;
    --teal: #00AB8E;
    --teal-bright: #00BBA5;
    --teal-soft: #67D7C9;
    --teal-pale: #C6EFE9;
    --teal-mist: #E9F9F6;
    --ink: #3c3c3c;
    --ink-soft: #555;
    --backdrop: #dcdcdc;
    --paper: #ffffff;
  }
  * { box-sizing: border-box; margin: 0; padding: 0; }
  html, body { width: 1200px; height: 960px; overflow: hidden; }
  body {
    background: var(--backdrop);
    display: flex; align-items: center; justify-content: center;
    font-family: "Open Sans", sans-serif;
  }
  .letterhead {
    position: relative;
    width: 636px; height: 900px;
    background: var(--paper);
    padding: 62px 60px 60px 64px;
    overflow: hidden;
    box-shadow: 0 2px 10px rgba(0,0,0,.12);
  }
  .watermark {
    position: absolute; right: -120px; bottom: 120px;
    width: 420px; height: 420px;
  }
  .header { display: flex; align-items: flex-start; gap: 28px; position: relative; }
  .brand { width: 210px; padding-top: 26px; display: flex; align-items: center; gap: 10px; }
  .brand-dot { width: 22px; height: 22px; border-radius: 50%; background: var(--teal); flex: none; }
  .brand-name {
    font-family: "Raleway", sans-serif; font-weight: 500;
    font-size: 30px; letter-spacing: 2px; color: var(--teal); line-height: 1;
  }
  .brand-tag {
    font-family: "Raleway", sans-serif; font-weight: 500;
    font-size: 10.5px; letter-spacing: 4.2px; color: var(--teal); margin-top: 5px;
  }
  .contact {
    border-left: 1.5px solid var(--teal-dark);
    padding: 4px 0 6px 16px;
    font-family: "Raleway", sans-serif; font-size: 12px; color: var(--ink); line-height: 1.35;
  }
  .contact-address { margin-bottom: 12px; }
  .contact-line { display: flex; align-items: center; gap: 6px; }
  .contact-line svg { width: 10px; height: 10px; flex: none; }
  .recipient { margin-top: 64px; position: relative; }
  .recipient-name {
    font-family: "Raleway", sans-serif; font-weight: 500; font-size: 14px;
    letter-spacing: .5px; color: var(--ink);
  }
  .recipient-detail { font-size: 11px; color: var(--ink-soft); line-height: 1.45; }
  .body { margin-top: 34px; font-size: 11px; line-height: 1.72; color: var(--ink); width: 440px; position: relative; }
  .body p { margin-bottom: 22px; }
  .closing { margin-top: 6px; font-size: 11px; color: var(--ink); position: relative; }
  .signature { display: block; width: 110px; height: 22px; margin: 16px 0 6px; }
  .sender-name { font-weight: 700; font-size: 13px; color: var(--teal-dark); }
</style>
</head>
<body>
  <main class="letterhead">
    <svg class="watermark" viewBox="0 0 420 420" role="img" aria-label="Faint brand emblem background decoration">
      <circle cx="210" cy="210" r="200" fill="var(--teal-mist)"/>
    </svg>

    <header class="header">
      <div class="brand">
        <span class="brand-dot"></span>
        <div>
          <div class="brand-name">KTNW</div>
          <div class="brand-tag">Financial Services</div>
        </div>
      </div>
      <address class="contact" style="font-style:normal">
        <div class="contact-address">PO Box 4187 Ashford<br>Vale NSW 2419</div>
        <div class="contact-line">
          <svg viewBox="0 0 10 10"><circle cx="5" cy="5" r="5" fill="var(--teal)"/><path d="M3 3.2c.4 1.6 1.4 2.8 3.8 3.6" stroke="#fff" stroke-width="1.2" fill="none" stroke-linecap="round"/></svg>
          (02) 5550 1862
        </div>
        <div class="contact-line">
          <svg viewBox="0 0 10 10"><rect x="0" y="1.5" width="10" height="7" rx="1" fill="var(--teal)"/><path d="M.5 2l4.5 3.5L9.5 2" stroke="#fff" stroke-width="1" fill="none"/></svg>
          hello@ktnwfinancial.com.au
        </div>
        <div class="contact-line">
          <svg viewBox="0 0 10 10"><circle cx="5" cy="5" r="5" fill="var(--teal)"/><ellipse cx="5" cy="5" rx="2" ry="4.2" stroke="#fff" stroke-width=".8" fill="none"/><path d="M1 5h8" stroke="#fff" stroke-width=".8"/></svg>
          www.ktnwfinancial.com.au
        </div>
      </address>
    </header>

    <section class="recipient">
      <div class="recipient-name">RENATA HOLLIS</div>
      <div class="recipient-detail">Chief Executive Officer<br>City/State, Zip Code</div>
    </section>

    <section class="body">
      <p>Proin gravida nibh vel velit auctor aliquet. Aenean sollicitudin, lorem quis bibendum auctor, nisi elit consequat ipsum, nec sagittis sem nibh id elit. Duis sed odio sit amet nibh vulputate cursus a sit amet mauris. Morbi accumsan ipsum velit. Nam nec tellus a odio tincidunt auctor a ornare odio. Sed non mauris vitae erat consequat auctor eu in elit. Class aptent taciti sociosqu ad litora torquent ugue. Sed non neque elit. Sed ut imperdiet nisi. Proin condimentum fermentum nunc. Etiam pharetra, imperdiet nisi. Proin condimentum fermentum nunc. Etiam pharetra, erat sed fermentum feugiat, velit mauris egestas quam, ut aliquam massa nisl quis neque. Suspendisse in orci enim.</p>
      <p>This is a sample version of Lorem Ipsum. Proin gravida nibh vel velit auctor aliquet. Aenean sollicitudin, lorem quis bibendum auctor, nisi elit consequat ipsum, nec sagittis sem nibh id elit. Duis sed odio sit amet nibh vulputate cursus a sit amet mauris. Morbi accumsan ipsum velit. Nam nec tellus a odio tincidunt auctor a ornare odio. Sed non mauris vitae erat consequat auctor eu in elit. Class aptent taciti sociosqu ad litora torquent per conubia nostra, per inceptos himenaeos. Mauris in erat justo.</p>
      <p>Nullam ac urna eu felis dapibus condimentum sit amet a augue. Sed non neque elit. Sed ut imperdiet nisi. Proin condimentum fermentum nunc. Etiam pharetra, erat sed fermentum feugiat, velit mauris egestas quam. Nullam ac urna eu felis dapibus condimentum sit amet a aug pharetra, erat sed fermentum feugiat, velit mauris egestas quam. Nullam ac urna eu felis dapibus condimentum sit amet a augue. Sed non neque elit. Sed ut imperdiet nisi. Proin condimentum fermentum nunc.</p>
    </section>

    <section class="closing">
      <div>Sincerely,</div>
      <svg class="signature" viewBox="0 0 110 22" role="img" aria-label="Handwritten signature">
        <rect x="0" y="8" width="110" height="8" rx="4" fill="var(--teal-pale)"/>
      </svg>
      <div class="sender-name">Dorian Valcourt</div>
    </section>
  </main>
</body>
</html>
```